RTV ELECTRICAL GROUP Website Providing Electrical Services

We're a company providing electrical services to the public. We're located in Bankstown a suburb in Sydney, Australia. We are a team of 4 electricians that provide service work to the public. We work on new construction buildings such as single story, double story & units. We also do office fit outs & commercial factory work.

Target Market(s)

All Age Groups
Construction People
Sydney, Australia

Industry/Entity Type

Electrical

Contact Information for Business Card

Name Gavin Lorrimer
Contact Number 0481 502 743
Company License 904517B
ABN 53 204 871 365
Residential Commercial Industrial
info@rtvelectrical.example.com.au

Coding

Coded - Design and coding required

Number of Pages Required

5+ page

Font styles to use
Serif
Sans Serif

Colors

Designer to choose colors to be used in the design.

Requirements
Must have
• WORDPRESS
• Nice & Simple
• Eye catching
• Easy to Read
• Contact details
• Instagram Linked
• Facebook Page Linked
• All Social Media Linked
• Live Chat
• Form Submission
• Testimonial
• Specify services Offered
• About Us (Company details)
• Industrial Installation Page
• Residential Installation Page
• Commercial Installation Page
• Mode of payment (cash, credit-debit card, cheque)
• Local & national electrical news
• Project Videos
• Newsletter
• Level 2 licensed accredited
• Project pictures and articles
• Awards
• Legalities (company's policy, terms, rules)
• FAQ's (Frequently asked questions)
• Collaboration Projects
• Careers
• Projects
• Suppliers
• Customer Perks (discounts or freebies)
• Employees Informations (pictures and basic information)
• Opening Hours and Map location
• Company Logo & Company License (owner license)
• Accreditation
• Customer Service
• Safety/Safety tips
• Clients information (regular clients)
• Expertise
• Company's processes
• Timeline page
• Homepage
• Specify installations
• Search toolbar
• Portfolio
• Request for an appointment - servicing
• Feedbacks
Nice to have
• Articles (better if recent project articles)
• Advertisement
• Influencer Quote
• Sneak Peeks (if you have new services offered)
• Staff Highlights
• Job Hiring (Career Growth)
• Ratings (Rate our service)
• A day/week in the work
• Personal Anecdotes
• Before and after post projects
• Ecological Values
• Marketing feature
• Tagline
• Streaming interactive videos
• Timeline
• Calendar
• Blog
• Emergency Services/Hotline
• Additional services offered
• Transportation (vehicle - car images of our company)
• Comment box (company - clients)
• Rate Us (Performance rating)
Should not have
• Website shouldn't be dark
• Website shouldn't be hard to read
• Advertisement of competitors
• Moving objects
• Dark background

```html
<!DOCTYPE html>
<html lang="en">
<head>
<meta charset="utf-8">
<title>RTV Electrical Group</title>
<link rel="stylesheet" href="https://fonts.googleapis.com/css2?family=Montserrat:wght@400;600;700&family=Open+Sans:wght@400;600;700&display=swap">
<style>
:root{
  --blue:#1b8fd2;
  --blue-light:#2aa3e4;
  --navy:#0b4d7d;
  --deep:#0f3d62;
  --process:#134a72;
  --ink:#222;
  --text:#555;
  --footer:#2c2c2c;
  --footer-line:#4a4a4a;
  --white:#fff;
}
*{box-sizing:border-box;margin:0;padding:0}
html,body{width:1200px;height:3636px;overflow:hidden}
body{position:relative;background:var(--white);font-family:"Open Sans",Arial,sans-serif;color:var(--text)}
.abs{position:absolute}
h1,h2,h3,h4,.heading{font-family:"Montserrat",Arial,sans-serif}

/* hero */
.hero{left:0;top:0;width:1200px;height:740px;background:linear-gradient(160deg,#8f8f8f 0%,#c9c9c9 35%,#a3a3a3 60%,#5e5e5e 100%)}
.hero-cut{left:0;top:0;width:1200px;height:740px}
.topbar{right:85px;top:24px;color:var(--white);font-weight:700;font-size:18px;display:flex;gap:18px;align-items:center}
.topbar svg{vertical-align:-3px;margin-right:6px}
.navbar{left:90px;top:68px;width:1025px;height:58px;background:var(--white);box-shadow:0 2px 8px rgba(0,0,0,.15)}
.nav{right:12px;top:0;height:58px;display:flex;align-items:center;gap:36px;font-family:"Montserrat",Arial,sans-serif;font-size:14px;font-weight:600;color:#222}
.nav .quote{background:var(--navy);color:var(--white);padding:9px 12px}
.logo-badge{left:84px;top:22px;width:160px;height:160px;border-radius:50%;background:var(--white);box-shadow:0 2px 10px rgba(0,0,0,.2);display:flex;align-items:center;justify-content:center;text-align:center;font-family:"Montserrat",Arial,sans-serif;font-weight:700;font-size:15px;line-height:1.3;color:var(--navy)}
.arrow-btn{width:34px;height:34px;border-radius:50%;background:#f2f2f2;top:370px;display:flex;align-items:center;justify-content:center}
.hero-box{left:90px;top:267px;width:572px;height:249px;background:rgba(27,143,210,.9);padding:26px 30px}
.hero-box h1{color:var(--white);font-size:50px;font-weight:700;line-height:1}
.hero-box p{color:var(--white);font-size:17px;font-weight:600;line-height:1.5;margin-top:12px}
.btn-dark{display:inline-block;background:var(--navy);color:var(--white);font-family:"Montserrat",Arial,sans-serif;font-weight:600;font-size:17px;padding:14px 22px}
.hero-box .btn-dark{margin-top:18px}

/* welcome */
.welcome{left:0;top:722px;width:1200px;text-align:center}
.welcome .pre{font-family:"Montserrat",Arial,sans-serif;font-size:28px;color:#222;letter-spacing:1px}
.welcome h2{font-size:52px;font-weight:600;color:var(--navy);letter-spacing:1px;display:flex;align-items:center;justify-content:center;gap:26px;margin-top:2px}
.welcome h2::before,.welcome h2::after{content:"";width:130px;height:2px;background:#333}
.welcome p{width:1000px;margin:20px auto 0;font-size:15.5px;line-height:1.9;color:#555}
.welcome .btn-dark{margin-top:28px;font-size:18px;padding:12px 22px}

/* services */
.services-bg{left:0;top:1030px;width:1200px;height:690px;background:linear-gradient(180deg,#1f6fa6 0%,#1b5d8d 45%,#164e78 100%)}
.services-cut{left:0;top:1000px;width:1200px;height:240px}
.offer{left:85px;top:1314px;width:247px;height:310px;background:rgba(31,147,215,.92);border:2px solid rgba(255,255,255,.5);text-align:center;padding:62px 22px 0;color:var(--white)}
.offer h3{font-size:25px;font-weight:700}
.offer p{font-size:12.5px;line-height:1.65;margin-top:14px}
.btn-outline{display:inline-block;border:2px solid var(--white);color:var(--white);font-size:13px;font-weight:600;padding:4px 14px;margin-top:26px}
.service-card{top:1314px;width:245px;color:var(--white)}
.service-card .photo{width:245px;height:153px}
.service-card h3{font-size:20px;font-weight:600;margin-top:26px}
.service-card p{font-size:12.5px;line-height:1.6;margin-top:10px;color:#dbe9f4}
.service-card .more{font-size:12.5px;font-weight:600;margin-top:12px}

/* process */
.process-bg{left:0;top:1720px;width:1200px;height:930px;background:linear-gradient(180deg,#104670 0%,#1a5d8e 55%,#1e6aa0 100%)}
.process-cut{left:0;top:2400px;width:1200px;height:250px}
.process-title{left:0;top:1795px;width:1200px;display:flex;justify-content:center;align-items:center;gap:30px;font-size:38px;font-weight:700;color:var(--white);letter-spacing:1px}
.process-title::before,.process-title::after{content:"";width:150px;height:2px;background:rgba(255,255,255,.8)}
.process-title span{color:var(--blue-light)}
.step{width:190px;color:var(--white)}
.step h4{font-size:16px;font-weight:700}
.step p{font-size:11.5px;line-height:1.6;margin-top:8px;color:#dce8f2}
.step .more{font-size:11.5px;margin-top:14px}
.step.left{left:125px;text-align:left}
.step.left h4{text-align:right;padding-right:0}
.step.left .more{text-align:right;padding-right:0}
.step.right{left:885px}
.step.right .more{padding-left:0}
.icon-circle{width:82px;height:82px;border-radius:50%;background:var(--blue);border:3px solid var(--white);display:flex;align-items:center;justify-content:center}
.hub{left:463px;top:1966px;width:276px;height:276px;border-radius:50%;background:var(--white);border:8px solid var(--navy);box-shadow:0 0 0 6px var(--white);display:flex;align-items:center;justify-content:center;text-align:center;font-family:"Montserrat",Arial,sans-serif;font-weight:700;font-size:24px;line-height:1.3;color:var(--navy)}

/* news */
.news-title{left:0;top:2620px;width:1200px;display:flex;justify-content:center;align-items:center;gap:28px;font-size:38px;font-weight:700;color:#222}
.news-title::before,.news-title::after{content:"";width:120px;height:2px;background:#222}
.news-title span{color:var(--blue)}
.news-card{top:2695px;width:330px}
.news-card h3{font-size:19px;font-weight:600;color:#222}
.news-card .photo{margin-top:14px;width:330px;height:206px;border:1px solid #ccc;padding:4px;background:var(--white)}
.news-card .photo div{width:100%;height:100%}
.news-card p{font-size:12.5px;line-height:1.75;color:#666;margin-top:22px}
.news-card .more{font-size:12.5px;color:#333;margin-top:30px}

/* newsletter */
.newsletter{left:0;top:3176px;width:1200px;height:133px;background:linear-gradient(90deg,#1e82c3,#1b8fd2 50%,#1e82c3)}
.newsletter h3{position:absolute;left:223px;top:47px;font-size:28px;font-weight:600;color:var(--white)}
.newsletter .field{position:absolute;left:550px;top:51px;width:282px;height:46px;border:2px solid rgba(255,255,255,.7);color:#d7ebf8;font-size:13px;padding:13px 14px}
.newsletter .submit{position:absolute;left:848px;top:51px;width:127px;height:46px;background:var(--navy);color:var(--white);font-family:"Montserrat",Arial,sans-serif;font-weight:600;font-size:17px;display:flex;align-items:center;justify-content:center}

/* footer */
.footer{left:0;top:3309px;width:1200px;height:327px;background:var(--footer);color:#ddd}
.footer-brand{position:absolute;left:80px;top:110px;width:300px;text-align:center;font-family:"Montserrat",Arial,sans-serif;font-weight:600;font-size:26px;color:var(--white);letter-spacing:1px;line-height:1.4}
.vline{position:absolute;width:1px;background:var(--footer-line);top:40px;height:190px}
.contact{position:absolute;left:468px;top:38px;font-size:16px;line-height:1.5}
.contact h4{font-family:"Open Sans",Arial,sans-serif;font-weight:400;font-size:17px;color:#eee;margin-bottom:14px}
.contact .row{display:flex;gap:18px;margin-bottom:16px}
.contact svg{flex:none;margin-top:3px}
.links{position:absolute;left:1006px;top:38px;font-size:14px}
.links h4{font-family:"Open Sans",Arial,sans-serif;font-weight:400;font-size:17px;color:#eee;margin-bottom:12px}
.links li{list-style:none;margin-bottom:9px}
.links li::before{content:"> ";font-weight:700}
.footer-rule{position:absolute;left:85px;top:254px;width:1030px;height:1px;background:var(--footer-line)}
.copyright{position:absolute;left:85px;top:282px;font-size:14px;color:#ccc}
.social{position:absolute;left:990px;top:282px;display:flex;gap:16px}
.social i{display:block;width:16px;height:16px;border-radius:50%;background:#ddd}
</style>
</head>
<body>

<!-- Hero -->
<div class="abs hero" role="img" aria-label="Electrician in hard hat working on a ceiling light fitting"></div>
<svg class="abs hero-cut" width="1200" height="740" viewBox="0 0 1200 740" aria-hidden="true">
  <polygon points="0,740 740,520 1200,640 1200,740" fill="#fff"/>
</svg>

<div class="abs topbar">
  <span><svg width="16" height="16" viewBox="0 0 24 24"><path fill="#fff" d="M6.6 10.8a15 15 0 0 0 6.6 6.6l2.2-2.2c.3-.3.7-.4 1-.2 1.1.4 2.3.6 3.6.6.6 0 1 .4 1 1V20c0 .6-.4 1-1 1A17 17 0 0 1 3 4c0-.6.4-1 1-1h3.5c.6 0 1 .4 1 1 0 1.3.2 2.5.6 3.6.1.3 0 .7-.2 1z"/></svg>: 0481 502 743</span>
  <span>|</span>
  <span><svg width="18" height="14" viewBox="0 0 24 18"><rect x="1" y="1" width="22" height="16" rx="2" fill="#fff"/><path d="M2 2l10 8 10-8" stroke="#888" stroke-width="2" fill="none"/></svg>: info@rtvelectrical.example.com.au</span>
</div>

<div class="abs navbar">
  <nav class="abs nav">
    <span>HOME</span><span>ABOUT US</span><span>SERVICES</span><span>BLOG</span><span>CONTACT US</span><span class="quote">REQUEST A QUOTE</span>
  </nav>
</div>
<div class="abs logo-badge">RTV<br>ELECTRICAL<br>GROUP</div>

<div class="abs arrow-btn" style="left:22px"><svg width="16" height="16" viewBox="0 0 16 16"><path d="M10 3L5 8l5 5" stroke="#333" stroke-width="3" fill="none"/></svg></div>
<div class="abs arrow-btn" style="left:1140px"><svg width="16" height="16" viewBox="0 0 16 16"><path d="M6 3l5 5-5 5" stroke="#333" stroke-width="3" fill="none"/></svg></div>

<div class="abs hero-box">
  <h1>RTV ELECTRICAL</h1>
  <p>Lorem ipsum dolor sit amet, consectetur adipiscing elit, sed do eiusmod tempor incididunt ut labore et dolore magna aliqua.</p>
  <span class="btn-dark">Read More &gt;</span>
</div>

<!-- Welcome -->
<section class="abs welcome">
  <div class="pre">WELCOME TO</div>
  <h2>RTV ELECTRICAL</h2>
  <p>Contrary to popular belief, Lorem Ipsum is not simply random text. It has roots in a piece of classical Latin literature from 45 BC, making it over 2000 years old. Harold Brennick, a Latin professor at Fairhaven College in Virginia, looked up one of the more obscure Latin words, consectetur, from a Lorem Ipsum passage, and going through the cites of the word in classical literature, discovered the undoubtable source.</p>
  <span class="btn-dark">READ MORE RTV</span>
</section>

<!-- Services -->
<div class="abs services-bg" role="img" aria-label="Faded photo of electrical panels in blue tint"></div>
<svg class="abs services-cut" width="1200" height="240" viewBox="0 0 1200 240" aria-hidden="true">
  <polygon points="0,0 1200,0 1200,30 280,225 0,80" fill="#fff"/>
</svg>

<div class="abs offer">
  <h3>What We Offer?</h3>
  <p>Lorem Ipsum is simply dummy text of the printing and typesetting industry. Lorem Ipsum has been the industry's1500s</p>
  <span class="btn-outline">Read More &gt;</span>
</div>

<div class="abs service-card" style="left:347px">
  <div class="photo" role="img" aria-label="Electrician inspecting a switchboard" style="background:linear-gradient(135deg,#c9d2d8,#8fa1ad 60%,#c76a3a)"></div>
  <h3>Services Goes Here</h3>
  <p>Lorem Ipsum is simply dummy text of the printing and typesetting industry. Lorem Ipsum industry's1500s</p>
  <div class="more">Read More &gt;</div>
</div>
<div class="abs service-card" style="left:608px">
  <div class="photo" role="img" aria-label="Worker in orange safety gear with a laptop" style="background:linear-gradient(135deg,#9ec3de,#d9833a 55%,#7a8c99)"></div>
  <h3>Services Goes Here</h3>
  <p>Lorem Ipsum is simply dummy text of the printing and typesetting industry. Lorem Ipsum industry's1500s</p>
  <div class="more">Read More &gt;</div>
</div>
<div class="abs service-card" style="left:868px">
  <div class="photo" role="img" aria-label="Electrician in yellow hard hat wiring a panel" style="background:linear-gradient(135deg,#e8eef2,#9db8cc 55%,#2f6fb0)"></div>
  <h3>Services Goes Here</h3>
  <p>Lorem Ipsum is simply dummy text of the printing and typesetting industry. Lorem Ipsum industry's1500s</p>
  <div class="more">Read More &gt;</div>
</div>

<!-- Process -->
<div class="abs process-bg" role="img" aria-label="Faded photo of electrician tools in deep blue tint"></div>
<svg class="abs process-cut" width="1200" height="250" viewBox="0 0 1200 250" aria-hidden="true">
  <polygon points="0,240 870,25 1200,120 1200,250 0,250" fill="#fff"/>
</svg>

<h2 class="abs process-title">OUR <span>PROCESS</span></h2>

<div class="abs step left" style="top:1880px"><h4>TITLE GOES HERE</h4><p>Sed ut perspiciatis unde omnis iste natus error sit voluptatem accusan-tium doloremque laudantium,</p><div class="more">Read More &gt;</div></div>
<div class="abs step left" style="top:2050px"><h4>TITLE GOES HERE</h4><p>Sed ut perspiciatis unde omnis iste natus error sit voluptatem accusan-tium doloremque laudantium,</p><div class="more">Read More &gt;</div></div>
<div class="abs step left" style="top:2220px"><h4>TITLE GOES HERE</h4><p>Sed ut perspiciatis unde omnis iste natus error sit voluptatem accusan-tium doloremque laudantium,</p><div class="more">Read More &gt;</div></div>
<div class="abs step right" style="top:1880px"><h4>TITLE GOES HERE</h4><p>Sed ut perspiciatis unde omnis iste natus error sit voluptatem accusan-tium doloremque laudantium,</p><div class="more">Read More &gt;</div></div>
<div class="abs step right" style="top:2050px"><h4>TITLE GOES HERE</h4><p>Sed ut perspiciatis unde omnis iste natus error sit voluptatem accusan-tium doloremque laudantium,</p><div class="more">Read More &gt;</div></div>
<div class="abs step right" style="top:2220px"><h4>TITLE GOES HERE</h4><p>Sed ut perspiciatis unde omnis iste natus error sit voluptatem accusan-tium doloremque laudantium,</p><div class="more">Read More &gt;</div></div>

<!-- left icons -->
<div class="abs icon-circle" style="left:323px;top:1898px"><svg width="34" height="34" viewBox="0 0 24 24"><path fill="#fff" d="M13 2L5 14h6l-2 8 9-13h-6z"/></svg></div>
<div class="abs icon-circle" style="left:323px;top:2063px"><svg width="36" height="36" viewBox="0 0 24 24"><circle cx="12" cy="12" r="7" fill="none" stroke="#fff" stroke-width="4" stroke-dasharray="3 2.5"/><circle cx="12" cy="12" r="3.5" fill="none" stroke="#fff" stroke-width="2"/></svg></div>
<div class="abs icon-circle" style="left:323px;top:2233px"><svg width="30" height="34" viewBox="0 0 24 24"><path fill="#fff" d="M12 2a7 7 0 0 0-7 7c0 5 7 13 7 13s7-8 7-13a7 7 0 0 0-7-7zm0 9.5A2.5 2.5 0 1 1 12 6.5a2.5 2.5 0 0 1 0 5z"/></svg></div>
<!-- right icons -->
<div class="abs icon-circle" style="left:790px;top:1898px"><svg width="34" height="34" viewBox="0 0 24 24"><path d="M4 12l5 5L20 6" stroke="#fff" stroke-width="3.5" fill="none"/></svg></div>
<div class="abs icon-circle" style="left:790px;top:2063px"><svg width="36" height="36" viewBox="0 0 24 24"><circle cx="12" cy="12" r="7" fill="none" stroke="#fff" stroke-width="4" stroke-dasharray="3 2.5"/><circle cx="12" cy="12" r="3.5" fill="none" stroke="#fff" stroke-width="2"/></svg></div>
<div class="abs icon-circle" style="left:790px;top:2233px"><svg width="38" height="34" viewBox="0 0 28 24"><circle cx="14" cy="7" r="4" fill="#fff"/><circle cx="6" cy="10" r="3" fill="#fff"/><circle cx="22" cy="10" r="3" fill="#fff"/><path fill="#fff" d="M7 22a7 7 0 0 1 14 0zM1 21a5 5 0 0 1 6-5l-1 5zM27 21a5 5 0 0 0-6-5l1 5z"/></svg></div>

<!-- hub arrows -->
<svg class="abs" style="left:400px;top:1900px" width="402" height="410" viewBox="0 0 402 410" aria-hidden="true">
  <g stroke="#fff" stroke-width="4" fill="#fff">
    <line x1="201" y1="60" x2="201" y2="20"/><polygon points="191,24 201,8 211,24"/>
    <line x1="201" y1="350" x2="201" y2="390"/><polygon points="191,386 201,402 211,386"/>
    <line x1="60" y1="204" x2="20" y2="204"/><polygon points="24,194 8,204 24,214"/>
    <line x1="342" y1="204" x2="382" y2="204"/><polygon points="378,194 394,204 378,214"/>
    <line x1="98" y1="100" x2="68" y2="70"/><polygon points="62,80 58,60 78,64"/>
    <line x1="304" y1="100" x2="334" y2="70"/><polygon points="324,64 344,60 340,80"/>
    <line x1="98" y1="308" x2="68" y2="338"/><polygon points="62,328 58,348 78,344"/>
    <line x1="304" y1="308" x2="334" y2="338"/><polygon points="324,344 344,348 340,328"/>
  </g>
</svg>
<div class="abs hub">RTV<br>ELECTRICAL<br>GROUP</div>

<!-- News -->
<h2 class="abs news-title">Latest <span>News</span></h2>

<article class="abs news-card" style="left:85px">
  <h3>Lorem Ipsum is simply dummy</h3>
  <div class="photo"><div role="img" aria-label="Electrician testing a row of switchboards" style="background:linear-gradient(135deg,#dfe4e8,#aeb9c0 55%,#3c4f66)"></div></div>
  <p>Sed ut perspiciatis unde omnis iste natus error sit voluptatem accusantium doloremque laudantium, totam rem aperiam, eaque ipsa quae ab illo inven-tore veritatis et quasi architecto</p>
  <div class="more">Read More &gt;</div>
</article>
<article class="abs news-card" style="left:436px">
  <h3>Lorem Ipsum is simply dummy</h3>
  <div class="photo"><div role="img" aria-label="Electrician in blue overalls holding a clipboard" style="background:linear-gradient(135deg,#f1f1f1,#cfd6dc 50%,#2d5d96)"></div></div>
  <p>Sed ut perspiciatis unde omnis iste natus error sit voluptatem accusantium doloremque laudantium, totam rem aperiam, eaque ipsa quae ab illo inventore veritatis et quasi architecto</p>
  <div class="more">Read More &gt;</div>
</article>
<article class="abs news-card" style="left:785px">
  <h3>Lorem Ipsum is simply dummy</h3>
  <div class="photo"><div role="img" aria-label="Technician servicing a wall air conditioner" style="background:linear-gradient(135deg,#e3ebf3,#bccbd8 55%,#f4f4f4)"></div></div>
  <p>Sed ut perspiciatis unde omnis iste natus error sit voluptatem accusantium doloremque laudantium, totam rem aperiam, eaque ipsa quae ab illo inventore veritatis et quasi architecto</p>
  <div class="more">Read More &gt;</div>
</article>

<!-- Newsletter -->
<section class="abs newsletter">
  <h3>Read Our Newsletter</h3>
  <div class="field">Email Address</div>
  <div class="submit">SUBMIT</div>
</section>

<!-- Footer -->
<footer class="abs footer">
  <div class="footer-brand">RTV ELECTRICAL<br>GROUP</div>
  <div class="vline" style="left:388px"></div>
  <div class="contact">
    <h4>Contact Us:</h4>
    <div class="row"><svg width="14" height="18" viewBox="0 0 24 24"><path fill="#ddd" d="M12 2a7 7 0 0 0-7 7c0 5 7 13 7 13s7-8 7-13a7 7 0 0 0-7-7zm0 9.5A2.5 2.5 0 1 1 12 6.5a2.5 2.5 0 0 1 0 5z"/></svg><span>RTV Electrical<br>42 Chapel Road, Bankstown, Australia. 2200.</span></div>
    <div class="row"><svg width="16" height="16" viewBox="0 0 24 24"><path fill="#ddd" d="M6.6 10.8a15 15 0 0 0 6.6 6.6l2.2-2.2c.3-.3.7-.4 1-.2 1.1.4 2.3.6 3.6.6.6 0 1 .4 1 1V20c0 .6-.4 1-1 1A17 17 0 0 1 3 4c0-.6.4-1 1-1h3.5c.6 0 1 .4 1 1 0 1.3.2 2.5.6 3.6.1.3 0 .7-.2 1z"/></svg><span>0481 502 743</span></div>
    <div class="row"><svg width="16" height="13" viewBox="0 0 24 18"><rect x="1" y="1" width="22" height="16" rx="2" fill="#ddd"/><path d="M2 2l10 8 10-8" stroke="#2c2c2c" stroke-width="2" fill="none"/></svg><span>info@rtvelectrical.example.com.au</span></div>
  </div>
  <div class="vline" style="left:914px"></div>
  <div class="links">
    <h4>Quick Links:</h4>
    <ul><li>Home</li><li>About Us</li><li>Services</li><li>Blog</li><li>Contact Us</li></ul>
  </div>
  <div class="footer-rule"></div>
  <div class="copyright">Copyright © 2018 RTV Electrical. All rights reserved.</div>
  <div class="social" aria-label="Social links"><i></i><i></i><i></i><i></i></div>
</footer>

</body>
</html>
```